Seed Company Looking For a Soybean Seed Bag Design

We are are a regional seed company who is currently launching a new line of soybean products. The brand of the product will be Tru-Crop. We are looking for a custom design of a soybean bag measuring 16"x5"x30" (when constructed). We are looking for a modern design that's relatively loud, but not too busy. The proof needs to match with the attached template. We have also provided a proof of a previous bag project (Fox-Ridge-Standard) we've done to show how the artwork needs to be laid out. In no way does the new design need to resemble the example. Also attached are some other examples of seed bags.
Industry/Entity Type
Agriculture
Colors
Designer to choose colors to be used in the design.
Look and feel
Each slider illustrates characteristics of the customer's brand and the style your logo design should communicate.

```html
<!DOCTYPE html>
<html lang="en">
<head>
<meta charset="utf-8">
<title>Tru-Crop Soybean Seeds – Bag Dieline</title>
<link rel="stylesheet" href="https://fonts.googleapis.com/css2?family=Exo+2:wght@600;700;800&family=Libre+Baskerville&family=Roboto+Condensed:wght@400&display=swap">
<style>
  :root {
    --brand-green: #1f9a3f;
    --slate: #5e5f61;
    --paper: #ffffff;
    --stage: #e8e8e8;
    --ink: #555658;
    --bean-light: #e2b36d;
    --bean-dark: #b9823a;
    --sketch: #eeeeee;
    --badge-blue: #1d4fa3;
  }
  html, body {
    margin: 0;
    width: 945px;
    height: 1200px;
    overflow: hidden;
    background: var(--stage);
  }
  .canvas {
    position: relative;
    width: 945px;
    height: 1200px;
  }
  .dieline {
    position: absolute;
    left: 0;
    top: 271px;
    display: block;
  }
  .heading { font-family: "Exo 2", sans-serif; font-weight: 800; }
  .wordmark { font-family: "Exo 2", sans-serif; font-weight: 700; letter-spacing: 1px; }
  .tagline { font-family: "Roboto Condensed", sans-serif; font-size: 5.5px; letter-spacing: .3px; }
  .pill-label { font-family: "Libre Baskerville", serif; }
  .contact { font-family: "Roboto Condensed", sans-serif; font-size: 6.4px; }
</style>
</head>
<body>
<main class="canvas">
  <svg class="dieline" width="945" height="658" viewBox="0 0 945 658" xmlns="http://www.w3.org/2000/svg">
    <defs>
      <radialGradient id="bean-fill" cx="50%" cy="45%" r="60%">
        <stop offset="0%" stop-color="var(--bean-light)"/>
        <stop offset="100%" stop-color="var(--bean-dark)"/>
      </radialGradient>
      <path id="front-title-arc" d="M236,332 A138,138 0 0 0 512,332"/>
    </defs>

    <!-- bag flat background -->
    <rect class="bag-ground" width="945" height="658" fill="var(--brand-green)"/>

    <!-- side gusset (left) -->
    <g class="gusset gusset-left">
      <rect x="93" y="50" width="99" height="557" fill="var(--slate)"/>
      <path d="M93,50 H192 V393 C165,350 130,320 93,315 Z" fill="var(--paper)"/>
      <path d="M93,315 C130,320 165,350 192,393" fill="none" stroke="var(--brand-green)" stroke-width="2.5"/>
      <text class="heading" transform="translate(138,205) rotate(-90)" text-anchor="middle" font-size="21" fill="var(--ink)">SOYBEAN SEEDS</text>
      <g transform="translate(155,205) rotate(-90)">
        <rect x="-40" y="-9" width="80" height="18" rx="9" fill="var(--ink)"/>
        <text class="pill-label" x="0" y="3" text-anchor="middle" font-size="7.5" fill="var(--paper)">Premium Quality</text>
      </g>
      <text class="wordmark" transform="translate(140,490) rotate(-90)" text-anchor="middle" font-size="24" fill="var(--paper)">TRU-CROP</text>
      <text class="tagline" transform="translate(160,490) rotate(-90)" text-anchor="middle" fill="var(--paper)">— ROOTED IN FIELDS, GROWING PARTNERSHIPS —</text>
    </g>

    <!-- front panel -->
    <g class="front-panel">
      <rect x="215" y="50" width="318" height="557" fill="var(--slate)"/>
      <path d="M215,50 H533 V420 C533,490 460,536 374,536 C288,536 215,490 215,420 Z" fill="var(--paper)"/>
      <path d="M215,420 C215,490 288,536 374,536 C460,536 533,490 533,420" fill="none" stroke="var(--brand-green)" stroke-width="3"/>

      <text class="wordmark" x="374" y="160" text-anchor="middle" font-size="40" fill="var(--brand-green)">TRU-CROP</text>
      <text class="tagline" x="374" y="182" text-anchor="middle" fill="var(--ink)">— ROOTED IN FIELDS, GROWING PARTNERSHIPS —</text>

      <circle cx="374" cy="332" r="113" fill="var(--sketch)" role="img" aria-label="Line drawing of soybean pods and leaves ringing the seed photo"/>
      <circle cx="374" cy="332" r="76" fill="url(#bean-fill)" stroke="var(--brand-green)" stroke-width="2" role="img" aria-label="Photo of golden soybean seeds"/>

      <text class="heading" font-size="27" fill="var(--ink)" letter-spacing="1">
        <textPath href="#front-title-arc" startOffset="50%" text-anchor="middle">SOYBEAN SEEDS</textPath>
      </text>

      <rect x="321" y="489" width="106" height="22" rx="11" fill="var(--ink)"/>
      <text class="pill-label" x="374" y="504" text-anchor="middle" font-size="9.5" fill="var(--paper)">Premium Quality</text>

      <text class="contact" x="377" text-anchor="middle" fill="var(--paper)">
        <tspan x="377" y="556">Tru-Crop Seed Company</tspan>
        <tspan x="377" y="564">112 Furrow Lane • Tru-Crop Seed, WI 00000</tspan>
        <tspan x="377" y="572">555.018.2040 • sales@tru-cropseed.example</tspan>
        <tspan x="377" y="580">www.tru-cropseed.example</tspan>
      </text>
      <circle class="cert-badge" cx="487" cy="564" r="19" fill="var(--paper)" stroke="var(--badge-blue)" stroke-width="3"/>
    </g>

    <!-- side gusset (right) -->
    <g class="gusset gusset-right" transform="translate(462,0)">
      <rect x="93" y="50" width="99" height="557" fill="var(--slate)"/>
      <path d="M93,50 H192 V315 C150,320 110,350 93,393 Z" fill="var(--paper)"/>
      <path d="M93,393 C110,350 150,320 192,315" fill="none" stroke="var(--brand-green)" stroke-width="2.5"/>
      <text class="heading" transform="translate(138,205) rotate(-90)" text-anchor="middle" font-size="21" fill="var(--ink)">SOYBEAN SEEDS</text>
      <g transform="translate(155,205) rotate(-90)">
        <rect x="-40" y="-9" width="80" height="18" rx="9" fill="var(--ink)"/>
        <text class="pill-label" x="0" y="3" text-anchor="middle" font-size="7.5" fill="var(--paper)">Premium Quality</text>
      </g>
      <text class="wordmark" transform="translate(140,490) rotate(-90)" text-anchor="middle" font-size="24" fill="var(--paper)">TRU-CROP</text>
      <text class="tagline" transform="translate(160,490) rotate(-90)" text-anchor="middle" fill="var(--paper)">— ROOTED IN FIELDS, GROWING PARTNERSHIPS —</text>
    </g>

    <!-- back panel -->
    <g class="back-panel">
      <rect x="731" y="50" width="214" height="557" fill="var(--paper)"/>
      <path d="M731,607 V301 C830,301 915,360 945,437 V607 Z" fill="var(--slate)"/>
      <path d="M731,301 C830,301 915,360 945,437" fill="none" stroke="var(--brand-green)" stroke-width="2.5"/>
    </g>
  </svg>
</main>
</body>
</html>
```